Design personal page for IT Expert

I'm freelancer in the area of IT Architecture/Cloud Computing/DevOps. <br/>Already have own page: www.brevantu.cc<br/><br/>I want to update/redesign it and have following sections/pages there:<br/>1) My short bio/details/soft skills<br/>2) List of my hard skills<br/>3) My key clients/success stories/feedbacks<br/>4) List of my conference talks with links/embedded youtube video<br/>5) List of my articles with links (probably article text on sub-page like blog)<br/><br/>Design should be compatible with wix.com (gona have premium plan there)<br/>

Number of Pages Required

4 page

Font styles to use
Sans Serif

Colors

Designer to choose colors to be used in the design.

Requirements
Must have
• 1) My short bio/details/soft skills
• 2) List of my hard skills
• 3) My key clients/success stories/feedbacks
• 4) List of my conference talks with links/embedded youtube video
• 5) List of my articles with links (probably article text on sub-page like blog)
Should not have
• No direct contact to my skype/email. I prefer to use this platform for my task discussion.

```html
<!DOCTYPE html>
<html lang="en">
<head>
<meta charset="utf-8">
<title>Marek Brevant — Cloud DevOps & Architect</title>
<link href="https://fonts.googleapis.com/css2?family=Poppins:wght@300;400;500;600;700;800&family=Playfair+Display:wght@400;700&display=swap" rel="stylesheet">
<style>
:root{
  --accent:#f47a55;
  --side:#2b2a2a;
  --hero:#1b1a1a;
  --ink:#2a2a2a;
  --muted:#9a9a9a;
  --line:#e9e9e9;
  --paper:#ffffff;
  --paper-soft:#f9f9f9;
}
*{margin:0;padding:0;box-sizing:border-box}
html,body{width:1200px;height:3303px;overflow:hidden;background:#fff}
body{font-family:"Poppins",sans-serif;color:var(--ink);position:relative}
.screen{position:absolute;left:0;width:1200px;overflow:hidden}
.screen-home{top:0;height:819px;background:var(--hero)}
.screen-about{top:827px;height:1161px;background:var(--paper)}
.screen-resume{top:1996px;height:1307px;background:var(--paper-soft)}

/* sidebar */
.sidebar{position:absolute;left:0;top:0;width:236px;height:100%;background:var(--side);text-align:center;color:#fff}
.avatar{position:absolute;left:73px;top:60px;width:90px;height:90px;border-radius:50%;border:4px solid #6c6c6c;background:radial-gradient(circle at 50% 40%,#d9d9d9,#8d8d8d)}
.sidebar .name{position:absolute;top:168px;width:100%;font-weight:700;font-size:14px}
.sidebar .role{position:absolute;width:100%;font-size:10px;color:#d8d8d8}
.sidebar .role.r1{top:195px}.sidebar .role.r2{top:215px}
.sidebar .rule{position:absolute;left:40px;width:156px;height:1px;background:#363535}
.nav{list-style:none}
.nav li{position:absolute;width:100%;font-size:12px;font-weight:500;text-transform:uppercase;letter-spacing:.2px}
.nav li.active{color:var(--accent);text-decoration:underline;text-underline-offset:4px}
.connect{position:absolute;top:597px;width:100%;font-size:10px;color:#d0d0d0}
.social{position:absolute;top:621px;left:96px;display:flex;gap:8px}
.social span{width:17px;height:17px;background:#3d3c3c;display:flex;align-items:center;justify-content:center}
.social span i{width:5px;height:5px;background:var(--accent);border-radius:50%}
.rights{position:absolute;bottom:8px;width:100%;font-size:8px;color:#6f6f6f;letter-spacing:.3px}

/* hero */
.hero-bg{position:absolute;left:236px;top:0;width:964px;height:819px;background:radial-gradient(ellipse 60% 55% at 35% 40%,#4a2417 0%,#2b1c17 45%,#1b1a1a 80%)}
.hero-title{position:absolute;left:236px;width:964px;top:323px;text-align:center;font-weight:800;font-size:47px;color:var(--accent);text-shadow:2px 2px 0 rgba(0,0,0,.35)}
.hero-rule{position:absolute;left:643px;top:397px;width:150px;height:1px;background:#5a5a5a}
.hero-sub{position:absolute;left:236px;width:964px;top:409px;text-align:center;color:#fff;font-size:21px;font-weight:600;letter-spacing:5px}
.btn{position:absolute;height:37px;display:flex;align-items:center;justify-content:center;font-size:10px;font-weight:600;text-transform:uppercase;letter-spacing:.3px}
.btn-solid{background:var(--accent);color:#fff}
.btn-outline{border:2px solid var(--accent);color:var(--accent)}

/* headings */
.section-title{position:absolute;left:236px;width:964px;text-align:center;font-family:"Playfair Display",serif;font-size:32px;color:var(--ink)}
.section-title::after{content:"";display:block;width:150px;height:1px;background:#d8d8d8;margin:6px auto 0}

/* about */
.about-photo{position:absolute;left:304px;top:188px;width:359px;height:216px;background:linear-gradient(135deg,#a9a9a9,#7d7d7d 55%,#5e5e5e)}
.about-lead{position:absolute;left:686px;top:185px;font-size:10px;font-weight:500}
.about-text{position:absolute;left:686px;top:226px;width:420px;font-size:9.5px;line-height:18px;color:#a8a8a8;font-weight:300}
.detail{position:absolute;font-size:9.5px;font-weight:500}
.detail::before{content:"›";color:var(--accent);font-size:13px;margin-right:6px}
.detail em{font-style:normal;color:#a8a8a8;font-weight:300;margin-left:4px}
.detail a{color:#3a56c8}
.service{position:absolute;width:300px}
.service .icon{width:46px;height:46px;border-radius:50%;background:#f4f4f4;display:flex;align-items:center;justify-content:center}
.service .icon i{width:22px;height:22px;border:1.5px solid var(--accent);border-radius:4px}
.service h3{font-size:11.5px;font-weight:500;margin-top:14px}
.service h3::after{content:"";display:block;width:26px;height:2px;background:var(--accent);margin-top:10px}
.service p{font-size:9.5px;line-height:18px;color:#9a9a9a;font-weight:300;margin-top:12px;width:270px}

/* resume */
.col-label{position:absolute;top:186px;font-size:12px;font-weight:500;border-bottom:2px solid var(--accent);padding-bottom:1px}
.timeline{position:absolute;top:247px;width:1px;height:561px;background:var(--accent)}
.card{position:absolute;width:369px;height:123px;background:#fff;border:1px solid #eee;padding:0 22px}
.card::before{content:"";position:absolute;left:-22px;top:25px;border-left:9px solid var(--accent);border-top:5px solid transparent;border-bottom:5px solid transparent}
.card .date{margin-top:21px;font-size:10px;color:var(--accent);display:flex;align-items:center;gap:10px}
.card .date svg{width:13px;height:12px}
.card h4{margin-top:12px;font-size:11.5px;font-weight:500}
.card p{margin-top:6px;font-size:9.5px;line-height:18px;color:#555;font-weight:300}
.skills-title{position:absolute;left:236px;width:964px;top:850px;text-align:center;font-size:11px;font-weight:500}
.skills-title span{border-bottom:2px solid var(--accent);padding-bottom:2px}
.skill{position:absolute;width:384px}
.skill .head{display:flex;justify-content:space-between;font-size:10px;font-weight:500}
.skill .head b{font-weight:400;font-size:8px;color:#b0b0b0}
.skill .bar{margin-top:6px;height:6px;border:1px solid var(--accent);border-radius:4px;padding:1px}
.skill .bar i{display:block;height:2px;width:88%;background:var(--accent);border-radius:2px}
.skill p{margin-top:7px;text-align:center;font-size:8.5px;color:#555;font-weight:300;white-space:nowrap}
</style>
</head>
<body>

<!-- HOME -->
<section class="screen screen-home">
  <aside class="sidebar">
    <div class="avatar" role="img" aria-label="Portrait photo of Marek Brevant"></div>
    <div class="name">Marek Brevant</div>
    <div class="role r1">~Nimbra Cloud DevOps &amp; Architect</div>
    <div class="role r2">~CI/CD Automation Expert</div>
    <div class="rule" style="top:270px"></div>
    <ul class="nav">
      <li class="active" style="top:314px">Home</li>
      <li style="top:353px">About me</li>
      <li style="top:388px">Hard skills</li>
      <li style="top:423px">Successful stories</li>
      <li style="top:459px">Conference talks</li>
      <li style="top:496px">Articles/Blog</li>
    </ul>
    <div class="rule" style="top:557px"></div>
    <div class="connect">Connect With Me:</div>
    <div class="social"><span><i></i></span><span><i></i></span></div>
    <div class="rights">ALL RIGHTS RESERVED</div>
  </aside>
  <div class="hero-bg" role="img" aria-label="Dark background with glowing orange honeycomb pattern"></div>
  <h1 class="hero-title">HI, I’M MAREK BREVANT</h1>
  <div class="hero-rule"></div>
  <div class="hero-sub">WELCOME TO MY WEBSITE</div>
  <div class="btn btn-solid" style="left:567px;top:477px;width:129px">Download CV</div>
  <div class="btn btn-outline" style="left:718px;top:477px;width:129px">Hire me now</div>
</section>

<!-- ABOUT -->
<section class="screen screen-about">
  <aside class="sidebar">
    <div class="avatar" role="img" aria-label="Portrait photo of Marek Brevant"></div>
    <div class="name">Marek Brevant</div>
    <div class="role r1">~Nimbra Cloud DevOps &amp; Architect</div>
    <div class="role r2">~CI/CD Automation Expert</div>
    <div class="rule" style="top:270px"></div>
    <ul class="nav">
      <li style="top:314px">Home</li>
      <li class="active" style="top:349px">About me</li>
      <li style="top:388px">Hard skills</li>
      <li style="top:423px">Successful stories</li>
      <li style="top:459px">Conference talks</li>
      <li style="top:496px">Articles/Blog</li>
    </ul>
    <div class="rule" style="top:557px"></div>
    <div class="connect">Connect With Me:</div>
    <div class="social"><span><i></i></span><span><i></i></span></div>
    <div class="rights">ALL RIGHTS RESERVED</div>
  </aside>
  <h2 class="section-title" style="top:82px">The Story About Me</h2>
  <div class="about-photo" role="img" aria-label="Photo of a man in glasses and suit behind a laptop on a grey wall"></div>
  <div class="about-lead">I'm open for remote long and short-term contracts and jobs</div>
  <p class="about-text">Lorem ipsum dolor amet forage tilde man bun chillwave pinterest. Food truck hammock semiotics pork belly wolf. Celiac mustache wolf kitsch lyft chia PBR&amp;B four dollar toast tumeric 3 wolf moon, occupy biodiesel. Twee migas hell of 8-bit kombucha, air plant tofu edison bulb yuccie PBR&amp;B direct trade locavore cornhole mustache polo santo. Cordigan yr swag tumeric ennui, cray wayfarers lomo paleo schlitz kogi. Butcher</p>
  <div class="detail" style="left:686px;top:338px">Lorem Ipsum:<em>somecontenthere</em></div>
  <div class="detail" style="left:892px;top:338px">Telex:<em>@MarekBrevant</em></div>
  <div class="detail" style="left:686px;top:364px">Dolor Amet:<em>loremipsumdolor</em></div>
  <div class="detail" style="left:892px;top:364px">Gigwork:<em>marekbrevant</em></div>
  <div class="detail" style="left:686px;top:389px">Download CV Here: <a>Marek_Brevant_Profile.pdf</a></div>

  <div class="service" style="left:309px;top:480px"><div class="icon"><i></i></div><h3>Design &amp; Implementation</h3><p>Design and implementation of infrastructure solutions of any complexity with 16+ years</p></div>
  <div class="service" style="left:626px;top:480px"><div class="icon"><i></i></div><h3>Clouds-practitioner</h3><p>All cloud providers in the world including any sort of clouds</p></div>
  <div class="service" style="left:911px;top:480px"><div class="icon"><i></i></div><h3>Helmora Practicioner</h3><p>Design and implementation of infrastructure solutions of any complexity</p></div>

  <div class="service" style="left:309px;top:638px"><div class="icon"><i></i></div><h3>CI/CD Practices</h3><p>Implementation of full cycle CI/CD practices including any sort of practices</p></div>
  <div class="service" style="left:626px;top:636px"><div class="icon"><i></i></div><h3>IT Systems</h3><p>Information security of IT-systems including any sort of security method</p></div>
  <div class="service" style="left:911px;top:636px"><div class="icon"><i></i></div><h3>Cost Effective IT Solutions</h3><p>Implementation of cost-effective of any IT-solutions and efficient solutions</p></div>

  <div class="service" style="left:309px;top:792px"><div class="icon"><i></i></div><h3>Business continuity management</h3><p>Lorem ipsum dolor amet ningun postedam if any lorem ipsum is simply dummy text</p></div>
  <div class="service" style="left:626px;top:792px"><div class="icon"><i></i></div><h3>Modern Solutions</h3><p>Introduction of modern frameworks, tools and technologies</p></div>
  <div class="service" style="left:911px;top:792px"><div class="icon"><i></i></div><h3>Helmora Practicioner</h3><p>Design and implementation of infrastructure solutions of any complexity</p></div>

  <div class="service" style="left:309px;top:947px"><div class="icon"><i></i></div><h3>CI/CD Practices</h3><p>Scrum, Kanban</p></div>
  <div class="service" style="left:628px;top:946px"><div class="icon"><i></i></div><h3>Cross Functional</h3><p>Manage cross-functional and remote teams of up to 50 people</p></div>
  <div class="service" style="left:911px;top:944px"><div class="icon"><i></i></div><h3>Psychoanalyst</h3><p>Lorem ipsum dolor amet ningun postedam if any lorem ipsum is simply</p></div>
</section>

<!-- RESUME -->
<section class="screen screen-resume">
  <aside class="sidebar">
    <div class="avatar" role="img" aria-label="Portrait photo of Marek Brevant"></div>
    <div class="name">Marek Brevant</div>
    <div class="role r1">~Nimbra Cloud DevOps &amp; Architect</div>
    <div class="role r2">~CI/CD Automation Expert</div>
    <div class="rule" style="top:270px"></div>
    <ul class="nav">
      <li style="top:314px">Home</li>
      <li style="top:353px">About me</li>
      <li class="active" style="top:388px">Hard skills</li>
      <li style="top:423px">Successful stories</li>
      <li style="top:459px">Conference talks</li>
      <li style="top:496px">Articles/Blog</li>
    </ul>
    <div class="rule" style="top:557px"></div>
    <div class="connect">Connect With Me:</div>
    <div class="social"><span><i></i></span><span><i></i></span></div>
    <div class="rights">ALL RIGHTS RESERVED</div>
  </aside>
  <h2 class="section-title" style="top:82px">Resume</h2>
  <div class="col-label" style="left:314px">Education</div>
  <div class="col-label" style="left:729px">Experience</div>
  <div class="btn btn-solid" style="left:994px;top:188px;width:128px">Download CV</div>

  <div class="timeline" style="left:315px"></div>
  <div class="timeline" style="left:731px"></div>

  <div class="card" style="left:337px;top:247px"><div class="date"><svg viewBox="0 0 13 12"><rect x=".5" y="1.5" width="12" height="10" fill="none" stroke="#f47a55"/><line x1="0" y1="4.5" x2="13" y2="4.5" stroke="#f47a55"/></svg>2004-2006</div><h4>Lorem Ipsum Dolor Amet</h4><p>Lorem ipsum dolor sit amet, consectetur adipiscing elit. Integermat fermentum nibh et metus facilisis sollicitudin</p></div>
  <div class="card" style="left:337px;top:393px"><div class="date"><svg viewBox="0 0 13 12"><rect x=".5" y="1.5" width="12" height="10" fill="none" stroke="#f47a55"/><line x1="0" y1="4.5" x2="13" y2="4.5" stroke="#f47a55"/></svg>2004-2006</div><h4>Lorem Ipsum Dolor Amet</h4><p>Lorem ipsum dolor sit amet, consectetur adipiscing elit. Integermat fermentum nibh et metus facilisis sollicitudin</p></div>
  <div class="card" style="left:337px;top:539px"><div class="date"><svg viewBox="0 0 13 12"><rect x=".5" y="1.5" width="12" height="10" fill="none" stroke="#f47a55"/><line x1="0" y1="4.5" x2="13" y2="4.5" stroke="#f47a55"/></svg>2004-2006</div><h4>Lorem Ipsum Dolor Amet</h4><p>Lorem ipsum dolor sit amet, consectetur adipiscing elit. Integermat fermentum nibh et metus facilisis sollicitudin</p></div>
  <div class="card" style="left:337px;top:685px"><div class="date"><svg viewBox="0 0 13 12"><rect x=".5" y="1.5" width="12" height="10" fill="none" stroke="#f47a55"/><line x1="0" y1="4.5" x2="13" y2="4.5" stroke="#f47a55"/></svg>2004-2006</div><h4>Lorem Ipsum Dolor Amet</h4><p>Lorem ipsum dolor sit amet, consectetur adipiscing elit. Integermat fermentum nibh et metus facilisis sollicitudin</p></div>

  <div class="card" style="left:753px;top:247px"><div class="date"><svg viewBox="0 0 13 12"><rect x=".5" y="1.5" width="12" height="10" fill="none" stroke="#f47a55"/><line x1="0" y1="4.5" x2="13" y2="4.5" stroke="#f47a55"/></svg>2004-2006</div><h4>Lorem Ipsum Dolor Amet</h4><p>Lorem ipsum dolor sit amet, consectetur adipiscing elit. Integermat fermentum nibh et metus facilisis sollicitudin</p></div>
  <div class="card" style="left:753px;top:393px"><div class="date"><svg viewBox="0 0 13 12"><rect x=".5" y="1.5" width="12" height="10" fill="none" stroke="#f47a55"/><line x1="0" y1="4.5" x2="13" y2="4.5" stroke="#f47a55"/></svg>2004-2006</div><h4>Lorem Ipsum Dolor Amet</h4><p>Lorem ipsum dolor sit amet, consectetur adipiscing elit. Integermat fermentum nibh et metus facilisis sollicitudin</p></div>
  <div class="card" style="left:753px;top:539px"><div class="date"><svg viewBox="0 0 13 12"><rect x=".5" y="1.5" width="12" height="10" fill="none" stroke="#f47a55"/><line x1="0" y1="4.5" x2="13" y2="4.5" stroke="#f47a55"/></svg>2004-2006</div><h4>Lorem Ipsum Dolor Amet</h4><p>Lorem ipsum dolor sit amet, consectetur adipiscing elit. Integermat fermentum nibh et metus facilisis sollicitudin</p></div>
  <div class="card" style="left:753px;top:685px"><div class="date"><svg viewBox="0 0 13 12"><rect x=".5" y="1.5" width="12" height="10" fill="none" stroke="#f47a55"/><line x1="0" y1="4.5" x2="13" y2="4.5" stroke="#f47a55"/></svg>2004-2006</div><h4>Lorem Ipsum Dolor Amet</h4><p>Lorem ipsum dolor sit amet, consectetur adipiscing elit. Integermat fermentum nibh et metus facilisis sollicitudin</p></div>

  <div class="skills-title"><span>Hard Skills</span></div>

  <div class="skill" style="left:322px;top:910px"><div class="head">Cloud Providers<b>80%</b></div><div class="bar"><i></i></div><p>Nimbra Web Services, Skyvale Cloud Platform, Postel Cloud, Openfold Cloud</p></div>
  <div class="skill" style="left:322px;top:977px"><div class="head">Linux Fundamentals<b>80%</b></div><div class="bar"><i></i></div><p>Nimbra Linux/Debra/Umbra, Shell Scripting, Firewalls, Networking, Protocols TCP/UDP</p></div>
  <div class="skill" style="left:322px;top:1044px"><div class="head">CI/CD<b>80%</b></div><div class="bar"><i></i></div><p>Collect &amp; Plan Requirements, Fetch Code, Build App Modules, Release Versioning, etc</p></div>
  <div class="skill" style="left:322px;top:1108px"><div class="head">Monitoring<b>80%</b></div><div class="bar"><i></i></div><p>Metrion, Dashly, Nimbra Cloud Watch, Zabrix, Loglane, Fluxbit, Elastra - Kivera</p></div>
  <div class="skill" style="left:322px;top:1172px"><div class="head">Coding Languages<b>80%</b></div><div class="bar"><i></i></div><p>Javelin, Pyther 2/3, Shell, Nodal JS, Gopher, C/C++</p></div>

  <div class="skill" style="left:754px;top:910px"><div class="head">Configuration Managment<b>80%</b></div><div class="bar"><i></i></div><p>Terraplan, StackForm, Ansera, Dockyn, Marionet</p></div>
  <div class="skill" style="left:754px;top:979px"><div class="head">Tools<b>80%</b></div><div class="bar"><i></i></div><p>Pyra, Bundlo, Rakit, Mavra, Gradix, Antor, Helmo, Pakman</p></div>
  <div class="skill" style="left:754px;top:1044px"><div class="head">Load Balancing<b>80%</b></div><div class="bar"><i></i></div><p>Nimbra Network Load Balancer, Nimbra Application Load Balancer, HiProxy, Enginox</p></div>
  <div class="skill" style="left:754px;top:1108px"><div class="head">Integration<b>80%</b></div><div class="bar"><i></i></div><p>TrailCI, LoopCI, ForgeCI, Shiply, Dronic, Bambu, CrewCity, Butlr</p></div>
  <div class="skill" style="left:754px;top:1172px"><div class="head">Data<b>80%</b></div><div class="bar"><i></i></div><p>MyQuery, Auroria, Redix, MangoBase, DynaStore, Streamo/Keeperz, Cassiope</p></div>
</section>

</body>
</html>
```